Brackenfold Latches Business Cards

Need high quality business card designed around my company logo. Ideally the cards need to be a glossy black as the logo goes well with a black background.

The company is a Locksmithing business.

Domestic clients are Residential Home Owners and Landlords. Commercial clients are local businesses, estate agents, landlords, solicitors

Services offered :
Emergency Lock Out
New Lock Fitting & Replacement
High Security Upgrades
UPVC lock repairs
Mobile Key Cutting
Free Security Reviews

Qualificatons & Certifications:
Accredited Guild & Tower KSR Level 3, QTRB
Fully Insured
PVX Checked

Contact & Business Details:

Business Name : Brackenfold Latches
Name: Rob Fenwick
Tel: 01823 574419 Office / 07841592637 Mobile
Email: contact@brackenfoldlatches.com
Website: www.brackenfoldlatches.com

(please note that the website is currently under development and not available to view)

Locksmith

Name: Rob Fenwick

Services:
Emergency Lock Out
High Security Upgrades
UPVC lock repairs
Mobile Key Cutting
Free Security Reviews

• Ideally the cards should be a glossy black as the logo stands out better on a black background.

Logo on front and the word LOCKSMITH should be incorporated into the front design of the card.

Qualifications & Certifications on the back ideally along the top / bottom of the card or split (I.e along the top “ Accredited : Guild & Tower Level 3 , QTRB”
and along the bottom , “Fully Insured & PVX Checked”

Services offered ideally listed on the back of the card, preferably split into two columns. If possible the logo could also be incorporated onto the back of the card between the two services columns (I.e the services listed either side of the logo)
• On the back of the card, have the logo in the middle with the services listed either side of the logo I.e 3 services on left of logo and three to the right.

```html
<!DOCTYPE html>
<html lang="en">
<head>
<meta charset="utf-8">
<title>Brackenfold Latches Business Cards</title>
<link rel="stylesheet" href="https://fonts.googleapis.com/css2?family=Oswald:wght@600&family=Roboto:wght@400&family=Cormorant+Garamond:wght@600;700&display=swap">
<style>
  :root {
    --backdrop: #4a4a4a;
    --card-black: #1c1c1c;
    --card-black-deep: #161616;
    --gold-light: #f3d467;
    --gold-mid: #d9a93a;
    --gold-dark: #a9731f;
    --gold-text: #e0a93a;
    --ink: #1a1a1a;
    --white: #f4f4f4;
  }
  * { margin: 0; padding: 0; box-sizing: border-box; }
  html, body { width: 963px; height: 1200px; overflow: hidden; }
  body { background: var(--backdrop); position: relative; }

  .card {
    position: absolute;
    left: 223px;
    width: 576px;
    height: 328px;
    border-radius: 16px;
    overflow: hidden;
  }
  .card-front { top: 214px; background: var(--card-black); }
  .card-back { top: 628px; background: var(--card-black-deep); }

  .front-band { position: absolute; inset: 0; }

  .brand-mark {
    position: absolute;
    top: 70px; left: 0; width: 100%;
    text-align: center;
    font-family: "Cormorant Garamond", serif;
    font-weight: 700;
    font-size: 34px;
    color: var(--gold-mid);
  }
  .brand-tag {
    position: absolute;
    top: 146px; left: 0; width: 100%;
    text-align: center;
    font-family: "Cormorant Garamond", serif;
    font-weight: 700;
    font-size: 14px;
    letter-spacing: 2px;
    color: var(--gold-mid);
  }

  .identity {
    position: absolute;
    right: 334px; top: 246px;
    text-align: right;
    color: var(--ink);
  }
  .identity-company {
    font-family: "Oswald", sans-serif;
    font-weight: 600;
    font-size: 21px;
    line-height: 1.1;
    text-transform: uppercase;
  }
  .identity-name {
    font-family: "Roboto", sans-serif;
    font-size: 13px;
    margin-top: 2px;
  }
  .divider {
    position: absolute;
    left: 263px; top: 238px;
    width: 1px; height: 66px;
    background: var(--ink);
  }
  .contacts {
    position: absolute;
    left: 277px; top: 237px;
    list-style: none;
    font-family: "Roboto", sans-serif;
    font-size: 13px;
    color: var(--ink);
  }
  .contacts li { display: flex; align-items: center; height: 16.5px; }
  .contacts svg { width: 10px; height: 10px; margin-right: 8px; fill: var(--ink); }

  .accreditation {
    position: absolute;
    top: 26px; left: 0; width: 100%;
    text-align: center;
    font-family: "Cormorant Garamond", serif;
    font-weight: 600;
    font-size: 14px;
    color: var(--white);
  }
  .emblem {
    position: absolute;
    left: 219px; top: 78px;
    width: 140px; height: 140px;
    border-radius: 50%;
    border: 2px solid var(--gold-mid);
    display: flex; align-items: center; justify-content: center;
    text-align: center;
  }
  .emblem-name {
    font-family: "Cormorant Garamond", serif;
    font-weight: 700;
    font-size: 20px;
    line-height: 1.05;
    color: var(--gold-mid);
  }
  .services {
    position: absolute;
    top: 231px; left: 0; width: 100%;
    text-align: center;
    font-family: "Roboto", sans-serif;
    font-size: 13px;
    line-height: 16.5px;
    color: var(--white);
  }
  .assurance {
    position: absolute;
    top: 295px; left: 0; width: 100%;
    text-align: center;
    font-family: "Cormorant Garamond", serif;
    font-weight: 700;
    font-size: 13.5px;
    color: var(--gold-text);
  }
  .assurance svg { width: 7px; height: 10px; fill: var(--gold-text); vertical-align: -1px; margin: 0 2px; }
</style>
</head>
<body>
  <section class="card card-front">
    <svg class="front-band" viewBox="0 0 576 328" aria-hidden="true">
      <defs>
        <linearGradient id="goldSweep" x1="0" x2="1" y1="0" y2="0">
          <stop offset="0" stop-color="var(--gold-dark)"/>
          <stop offset="0.35" stop-color="var(--gold-light)"/>
          <stop offset="0.65" stop-color="var(--gold-light)"/>
          <stop offset="1" stop-color="var(--gold-dark)"/>
        </linearGradient>
      </defs>
      <path d="M0 128 Q288 282 576 122 L576 328 L0 328 Z" fill="url(#goldSweep)"/>
      <path d="M0 128 Q288 282 576 122" fill="none" stroke="#1a1a1a" stroke-width="1.5"/>
      <path d="M0 122 Q288 262 576 114" fill="none" stroke="url(#goldSweep)" stroke-width="2.5" stroke-dasharray="6 4"/>
    </svg>
    <div class="brand-mark">Brackenfold Latches</div>
    <div class="brand-tag">LOCKSMITH</div>

    <div class="identity">
      <div class="identity-company">Brackenfold Latches</div>
      <div class="identity-name">Rob Fenwick</div>
    </div>
    <div class="divider"></div>
    <ul class="contacts">
      <li><svg viewBox="0 0 10 10"><path d="M2 0 L4 2.5 L3 3.8 Q4.5 6 6.2 7 L7.5 6 L10 8 L8.5 10 Q3 9 0 1.5 Z"/></svg>01823 574419</li>
      <li><svg viewBox="0 0 10 10"><path d="M2.5 0 H7.5 V10 H2.5 Z M3.5 1 V8 H6.5 V1 Z"/></svg>07841592637</li>
      <li><svg viewBox="0 0 10 10"><path d="M0 2 H10 V8.5 H0 Z M0.5 2.5 L5 6 L9.5 2.5" stroke="#f3d467" stroke-width="0.8"/></svg>contact@brackenfoldlatches.com</li>
      <li><svg viewBox="0 0 10 10"><circle cx="5" cy="5" r="5"/><path d="M2 3 Q4 2 4 4 Q6 5 5 7 M6 1.5 Q7 3 8.5 3" stroke="#f3d467" stroke-width="0.9" fill="none"/></svg>www.brackenfoldlatches.com</li>
    </ul>
  </section>

  <section class="card card-back">
    <p class="accreditation">Accredited Guild &amp; Tower KSR Level 3, QTRB</p>
    <div class="emblem"><span class="emblem-name">Brackenfold<br>Latches</span></div>
    <p class="services">
      Emergency Lock Out | New Lock Fitting &amp; Replacement<br>
      High Security Upgrades | UPVC lock repairs | Mobile Key Cutting<br>
      Free Security Reviews
    </p>
    <p class="assurance">FULLY INSURED <svg viewBox="0 0 7 10"><circle cx="3.5" cy="2.5" r="2.5"/><rect x="2.5" y="3" width="2" height="7"/></svg> PVX CHECKED</p>
  </section>
</body>
</html>
```